Moltbeck Chardonnay Wine Label 2024

We need a wine label design for a small, family-owned vineyard in Broke, Hunter Valley of NSW (Australia). The vineyard is called Moltbeck and we have an existing logo and 'brand book' for the vineyard home that is rented out for short stay bookings. This is attached and includes font style, colour palette and our Moltbeck logo for the accommodation (we're not wedded to this but also probably not after a completely different rethink either as we want the accommodation and the wine to feel part of the same thing.

Project:
The initial label requirement (front and back) is for the Moltbeck 2024 Chardonnay, which is called 'Juniper'. The label would need to be able to extend to other varietals (eg Verdehlo and Sparkling) in 2025. Attached is draft copy for front and back for the 2024 Chardonnay as a guide.

STYLE: We like a relatively simple, classic design and have played with both a dark (navy) and a light background (white/cream). Based on the final label design we will order a Kortap colour to pick up on the label theme.

The Chardonnay bottle dimensions are attached, as is our logo file (if that helps)

online 25-50 yearold

Wine

• front and back label design Moltbeck logo and name

```html
<!DOCTYPE html>
<html lang="en">
<head>
<meta charset="utf-8">
<title>Moltbeck Juniper 2024 Chardonnay – Front Label</title>
<link rel="stylesheet" href="https://fonts.googleapis.com/css2?family=Cormorant+Garamond:wght@600&family=Montserrat:wght@600;700&display=swap">
<style>
  :root {
    --stage: #0b0d10;
    --label-navy: #1f2b3d;
    --label-navy-deep: #172131;
    --gold: #d9a93a;
    --art-blue: #3a78c9;
    --art-green: #8fb43a;
  }
  * { margin: 0; padding: 0; box-sizing: border-box; }
  html, body { width: 1200px; height: 1200px; overflow: hidden; background: var(--stage); }
  .canvas {
    width: 1200px; height: 1200px;
    display: flex; align-items: center; justify-content: center;
  }
  .label {
    position: relative;
    width: 780px; height: 1020px;
    background:
      repeating-linear-gradient(45deg, rgba(255,255,255,0.025) 0 2px, transparent 2px 5px),
      linear-gradient(180deg, var(--label-navy) 0%, var(--label-navy-deep) 100%);
    overflow: hidden;
  }
  .landscape-art {
    position: absolute;
    left: 60px; top: 60px;
    width: 660px; height: 580px;
    border-radius: 50%;
    background: linear-gradient(180deg, var(--art-blue) 0%, var(--art-green) 100%);
    opacity: 0.9;
  }
  .brand-block {
    position: absolute;
    right: 90px; bottom: 110px;
    text-align: right;
    color: var(--gold);
  }
  .brand-name {
    display: flex; align-items: center; justify-content: flex-end; gap: 16px;
    font-family: "Cormorant Garamond", serif;
    font-weight: 600;
    font-size: 92px;
    line-height: 1;
    color: var(--gold);
  }
  .brand-dot {
    width: 18px; height: 18px; border-radius: 50%;
    background: var(--gold);
  }
  .wine-name {
    margin-top: 10px;
    font-family: "Montserrat", sans-serif;
    font-weight: 700;
    font-size: 44px;
    letter-spacing: 4px;
    line-height: 1.1;
  }
  .wine-details {
    margin-top: 8px;
    font-family: "Montserrat", sans-serif;
    font-weight: 600;
    font-size: 24px;
    letter-spacing: 2px;
    line-height: 1.3;
  }
</style>
</head>
<body>
  <main class="canvas">
    <section class="label">
      <div class="landscape-art" role="img" aria-label="Painted landscape of the vineyard homestead among hills under a blue sky"></div>
      <div class="brand-block">
        <div class="brand-name"><span class="brand-dot"></span>Moltbeck</div>
        <div class="wine-name">JUNIPER</div>
        <div class="wine-details">2024 CHARDONNAY<br>HUNTER VALLEY</div>
      </div>
    </section>
  </main>
</body>
</html>
```